New Design for calculator landing page

I need an original design created for a calculator application on a website.
-It needs to incorporate colors and them from the main website (velmor.org).
-Base calculator on a design similar, but not exact as tqs.oruv.com/calculator.php
-Incorporate the company's logo and the arrow design from the logo in the overall layout (once again this can be found on velmor.org.

Number of Pages Required

2 page

Requirements
Must have
• Two Designs Needed:
• -1st) Design with the base calculator design before all of the variables are entered
• -2nd) Design after the variables are entered and the slider comes out
• Use tqs.oruv.com/calculator.php for reference. Notice that after you fill in the different variables, the calculator expands out. The 2nd design needs to be the same for our calculator.
• -Make sure VELMOR's contact email and phone number are at the bottom
• Phone: 318.645.2917
• Email: info@velmor.org
Should not have
• Don't work about any of the actual text in the calculator. That will be added in by the programmers. I just need the layout and design. (the only text that should be added is the email and phone number at the bottom)

```html
<!DOCTYPE html>
<html lang="en">
<head>
<meta charset="utf-8">
<title>Restraint Length Calculator</title>
<link href="https://fonts.googleapis.com/css2?family=Open+Sans:wght@400;700&family=Hind:wght@400&family=Raleway:wght@300;400&display=swap" rel="stylesheet">
<style>
  :root {
    --page-bg: #41b4e6;
    --page-line: rgba(255,255,255,0.14);
    --card-top: #d2edf8;
    --card-top-edge: #e4f4fb;
    --card-body: #bde5f5;
    --field: #ffffff;
    --accent-green: #7dbe3f;
    --title: #eaf6fc;
    --label: #2f4752;
    --muted-icon: #9fb3bb;
    --nav: #5d7580;
    --ink: #2b3940;
    --logo-ink: #3a3a3a;
  }
  * { box-sizing: border-box; margin: 0; padding: 0; }
  html, body { width: 1200px; height: 989px; overflow: hidden; }
  body {
    position: relative;
    background: var(--page-bg);
    font-family: "Hind", "Open Sans", sans-serif;
  }
  .backdrop { position: absolute; inset: 0; }

  .brand {
    position: absolute; left: 97px; top: 412px;
    display: flex; align-items: center; gap: 12px;
    font-family: "Open Sans", sans-serif; font-weight: 400;
    font-size: 40px; letter-spacing: 1px; color: var(--logo-ink);
  }
  .brand-dot { width: 14px; height: 14px; border-radius: 50%; background: var(--logo-ink); }

  .page-title {
    position: absolute; left: 401px; top: 104px;
    font-family: "Open Sans", sans-serif; color: var(--title);
    white-space: nowrap;
  }
  .page-title strong { font-weight: 700; font-size: 29px; }
  .page-title span { font-weight: 400; font-size: 23px; margin-left: 4px; }

  .calculator {
    position: absolute; left: 400px; top: 157px; width: 402px; height: 626px;
    background: var(--card-body);
    box-shadow: 0 16px 50px rgba(20,80,120,0.35);
  }
  .project-panel {
    position: relative; height: 161px;
    background: var(--card-top);
    border-top: 4px solid var(--card-top-edge);
  }
  .label {
    position: absolute; font-size: 13px; color: var(--label); line-height: 1;
  }
  .field {
    position: absolute; width: 191px; height: 32px; background: var(--field);
  }
  .note { position: absolute; left: 341px; font-size: 13px; color: var(--label); }

  .item-controls {
    position: absolute; top: 128px; left: 0; width: 100%; height: 18px;
  }
  .item-controls svg { position: absolute; top: 0; }
  .item-count {
    position: absolute; left: 250px; top: 2px; font-size: 12px; color: var(--nav);
  }

  .inputs { position: relative; }
  .help { position: absolute; left: 154px; width: 15px; height: 15px; }
  .select-arrow { position: absolute; right: 10px; top: 12px; }

  .green-bar {
    position: absolute; left: 0; bottom: 0; width: 100%; height: 8px;
    background: var(--accent-green);
  }

  .contact {
    position: absolute; top: 802px; font-family: "Raleway", sans-serif;
    font-weight: 400; font-size: 26px; color: var(--ink); letter-spacing: -0.3px;
  }
  .contact-phone { left: 399px; }
  .contact-email { right: 396px; }
</style>
</head>
<body>
  <svg class="backdrop" width="1200" height="989" viewBox="0 0 1200 989" aria-hidden="true">
    <g fill="none" stroke="var(--page-line)" stroke-width="2">
      <line x1="900" y1="0" x2="1200" y2="180"/>
      <line x1="760" y1="320" x2="1060" y2="0"/>
      <line x1="0" y1="720" x2="92" y2="812"/>
      <line x1="0" y1="940" x2="50" y2="989"/>
      <line x1="280" y1="989" x2="470" y2="800"/>
    </g>
  </svg>

  <div class="brand"><span class="brand-dot"></span>VELMOR</div>

  <h1 class="page-title"><strong>Restraint Length</strong><span>Calculator</span></h1>

  <main class="calculator">
    <section class="project-panel">
      <span class="label" style="left:24px;top:50px">Project Name</span>
      <div class="field" style="left:132px;top:35px"></div>
      <span class="note" style="top:50px">Note</span>

      <span class="label" style="left:24px;top:88px">Site Name</span>
      <div class="field" style="left:132px;top:75px"></div>
      <span class="note" style="top:88px">Note</span>

      <div class="item-controls">
        <svg style="left:132px" width="16" height="16" viewBox="0 0 16 16" aria-label="Add item"><circle cx="8" cy="8" r="6.5" fill="none" stroke="#1f2b30" stroke-width="1.4"/><path d="M8 4.8v6.4M4.8 8h6.4" stroke="#1f2b30" stroke-width="1.4"/></svg>
        <svg style="left:156px" width="16" height="16" viewBox="0 0 16 16" aria-label="Remove item"><circle cx="8" cy="8" r="6.5" fill="none" stroke="#1f2b30" stroke-width="1.4"/><path d="M4.8 8h6.4" stroke="#1f2b30" stroke-width="1.4"/></svg>
        <svg style="left:224px;top:1px" width="14" height="14" viewBox="0 0 14 14" aria-label="Previous item"><path d="M12 7H2M6.5 2.5L2 7l4.5 4.5" fill="none" stroke="var(--nav)" stroke-width="1.6"/></svg>
        <span class="item-count">Item 1 of 1</span>
        <svg style="left:311px;top:1px" width="14" height="14" viewBox="0 0 14 14" aria-label="Next item"><path d="M2 7h10M7.5 2.5L12 7l-4.5 4.5" fill="none" stroke="var(--nav)" stroke-width="1.6"/></svg>
      </div>
    </section>

    <section class="inputs">
      <span class="label" style="left:25px;top:44px">Pipe Material</span>
      <svg class="help" style="top:40px" viewBox="0 0 15 15"><circle cx="7.5" cy="7.5" r="6.7" fill="none" stroke="var(--muted-icon)"/><text x="7.5" y="11" font-size="9" text-anchor="middle" fill="var(--muted-icon)" font-family="Open Sans, sans-serif">?</text></svg>
      <div class="field" style="left:189px;top:28px">
        <svg class="select-arrow" width="10" height="8" viewBox="0 0 10 8"><path d="M0 0h10L5 8z" fill="var(--accent-green)"/></svg>
      </div>

      <span class="label" style="left:25px;top:92px">Soil Type</span>
      <svg class="help" style="top:90px" viewBox="0 0 15 15"><circle cx="7.5" cy="7.5" r="6.7" fill="none" stroke="var(--muted-icon)"/><text x="7.5" y="11" font-size="9" text-anchor="middle" fill="var(--muted-icon)" font-family="Open Sans, sans-serif">?</text></svg>
      <div class="field" style="left:189px;top:76px"></div>

      <span class="label" style="left:25px;top:139px">Safety Factor</span>
      <svg class="help" style="top:136px" viewBox="0 0 15 15"><circle cx="7.5" cy="7.5" r="6.7" fill="none" stroke="var(--muted-icon)"/><text x="7.5" y="11" font-size="9" text-anchor="middle" fill="var(--muted-icon)" font-family="Open Sans, sans-serif">?</text></svg>
      <div class="field" style="left:189px;top:124px"></div>

      <span class="label" style="left:25px;top:186px">Trench Type</span>
      <svg class="help" style="top:184px" viewBox="0 0 15 15"><circle cx="7.5" cy="7.5" r="6.7" fill="none" stroke="var(--muted-icon)"/><text x="7.5" y="11" font-size="9" text-anchor="middle" fill="var(--muted-icon)" font-family="Open Sans, sans-serif">?</text></svg>
      <div class="field" style="left:189px;top:171px"></div>

      <span class="label" style="left:25px;top:233px">Depth of Bury</span>
      <svg class="help" style="top:231px" viewBox="0 0 15 15"><circle cx="7.5" cy="7.5" r="6.7" fill="none" stroke="var(--muted-icon)"/><text x="7.5" y="11" font-size="9" text-anchor="middle" fill="var(--muted-icon)" font-family="Open Sans, sans-serif">?</text></svg>
      <div class="field" style="left:189px;top:219px"></div>

      <span class="label" style="left:25px;top:280px">Test Pressure</span>
      <svg class="help" style="top:278px" viewBox="0 0 15 15"><circle cx="7.5" cy="7.5" r="6.7" fill="none" stroke="var(--muted-icon)"/><text x="7.5" y="11" font-size="9" text-anchor="middle" fill="var(--muted-icon)" font-family="Open Sans, sans-serif">?</text></svg>
      <div class="field" style="left:189px;top:267px"></div>

      <span class="label" style="left:25px;top:327px">Fitting Type</span>
      <svg class="help" style="top:326px" viewBox="0 0 15 15"><circle cx="7.5" cy="7.5" r="6.7" fill="none" stroke="var(--muted-icon)"/><text x="7.5" y="11" font-size="9" text-anchor="middle" fill="var(--muted-icon)" font-family="Open Sans, sans-serif">?</text></svg>
      <div class="field" style="left:189px;top:315px"></div>
    </section>

    <div class="green-bar"></div>
  </main>

  <span class="contact contact-phone">318.645.2917</span>
  <span class="contact contact-email">info@velmor.org</span>
</body>
</html>
```